Tavok Construction we build lodges in Botswana

We need a Design Layout only with Categories where we can update each projects photos.... We have a web address and a host - tavok.construction

```html
<!DOCTYPE html>
<html lang="en">
<head>
<meta charset="utf-8">
<title>Tavok Construction</title>
<link href="https://fonts.googleapis.com/css2?family=Montserrat:wght@400;500;600;700&family=Open+Sans:wght@400;600;700&display=swap" rel="stylesheet">
<style>
:root{
  --green:#25c35f;
  --green-dark:#1ba84f;
  --navy:#0c2547;
  --navy-deep:#081b36;
  --ink:#2b2f36;
  --muted:#7b8089;
  --line:#e2e4e8;
  --grey-bg:#f3f3f3;
  --white:#ffffff;
}
*{box-sizing:border-box;margin:0;padding:0}
html,body{width:1200px;height:3076px;overflow:hidden}
body{font-family:"Open Sans",Arial,sans-serif;color:var(--ink);background:var(--white);position:relative}
h1,h2,h3,.brand,.nav a,.btn{font-family:"Montserrat",Arial,sans-serif}
.section{position:absolute;left:0;width:1200px}

/* hero */
.hero{top:0;height:690px;overflow:hidden}
.hero-photo{position:absolute;inset:0 0 40px 0;background:linear-gradient(160deg,#3a2a1e 0%,#5b4330 35%,#2a2520 70%,#1b1a18 100%)}
.hero-shade{position:absolute;inset:0 0 40px 0;background:rgba(10,10,10,.35)}
.hero-edge{position:absolute;left:0;bottom:0;width:1200px;height:140px}
.brand-bar{position:absolute;top:38px;left:40px}
.brand{font-size:26px;font-weight:700;color:var(--white);letter-spacing:.5px}
.nav{position:absolute;top:46px;right:50px;display:flex;gap:38px}
.nav a{color:var(--white);font-size:13px;font-weight:600;text-decoration:none;letter-spacing:.5px}
.nav a.active{color:var(--green)}
.hero-copy{position:absolute;top:270px;left:0;width:1200px;text-align:center;color:var(--white)}
.hero-copy h1{font-size:40px;font-weight:700;letter-spacing:1px}
.hero-copy p{width:520px;margin:18px auto 0;font-size:20px;line-height:28px}
.btn{display:inline-block;font-size:14px;font-weight:600;letter-spacing:.5px;border-radius:30px;color:var(--white);text-decoration:none}
.btn-green{background:var(--green);padding:16px 40px;margin-top:26px}
.btn-navy{background:var(--navy);padding:16px 32px}

/* section headings */
.heading{text-align:center}
.heading h2{font-size:40px;font-weight:500;color:var(--ink);letter-spacing:1px}
.rule{display:block;width:60px;height:3px;background:var(--green);margin:14px auto 0}
.intro{font-size:13px;color:var(--muted);text-align:center;margin-top:16px}

/* services */
.services{top:690px;height:610px}
.services .heading{position:absolute;top:30px;width:1200px}
.service-card{position:absolute;width:362px;height:152px;background:var(--white);border:1px solid var(--line);border-left:3px solid var(--green);padding:22px 22px 0 96px}
.service-card h3{font-size:14px;font-weight:600;letter-spacing:.5px;color:var(--ink)}
.service-card p{font-size:12px;line-height:20px;color:var(--muted);margin-top:10px}
.service-card .more{color:var(--green);font-weight:700;font-size:11px}
.service-icon{position:absolute;left:26px;top:26px;width:48px;height:48px}
.service-card.right{padding:22px 96px 0 22px;border-left:1px solid var(--line);border-right:3px solid var(--green)}
.service-card.right .service-icon{left:auto;right:26px}
.worker{position:absolute;left:478px;top:130px;width:244px;height:480px;border-radius:120px 120px 0 0;background:linear-gradient(180deg,#f2c230 0%,#2d3f6b 40%,#1e2a48 100%)}

/* about */
.about{top:1300px;height:445px;background:var(--grey-bg)}
.about-copy{position:absolute;left:110px;top:70px;width:400px}
.about-copy h2{font-size:42px;font-weight:500;letter-spacing:1px}
.about-copy .rule{margin:14px 0 0}
.about-copy p{font-size:13px;line-height:22px;color:var(--muted);margin-top:24px}
.about-copy .btn{margin-top:38px}
.about-art{position:absolute;left:540px;top:40px;width:590px;height:370px;background:linear-gradient(180deg,#f3f3f3 0%,#d8d8d8 55%,#9c9c9c 100%)}

/* projects */
.projects{top:1745px;height:555px}
.projects .heading{position:absolute;top:30px;width:1200px}
.collage{position:absolute;left:0;top:0;width:1200px;height:555px}

/* testimonial */
.testimonial{top:2300px;height:340px;background:linear-gradient(90deg,var(--green-dark),var(--green))}
.quote{position:absolute;left:200px;top:70px;width:560px;color:var(--white)}
.quote p{font-size:13px;line-height:22px}
.quote .name{font-family:"Montserrat",Arial,sans-serif;font-weight:700;font-size:13px;margin-top:30px;letter-spacing:.5px}
.quote .role{font-size:11px;opacity:.85;margin-top:4px}
.portrait{position:absolute;left:812px;top:70px;width:200px;height:200px;border-radius:50%;border:6px solid var(--white);background:linear-gradient(160deg,#b88563,#5a3b2c)}

/* footer */
.footer{top:2640px;height:436px;background:var(--navy)}
.col{position:absolute;top:60px;color:var(--white)}
.col h3{font-size:16px;font-weight:600;letter-spacing:.5px;margin-bottom:22px}
.col p,.col li{font-size:12px;line-height:20px;color:#c9d2e0}
.col ul{list-style:none}
.col li{margin-bottom:6px}
.footer .brand{font-size:26px;font-weight:500;color:var(--green)}
.col .label{color:var(--white);font-weight:600;font-size:11px;margin-top:14px}
.col .label:first-child{margin-top:0}
.read{color:var(--green);font-size:12px;margin-top:10px}
.email-field{width:240px;height:36px;background:var(--white);border:none;font-size:11px;color:var(--muted);padding:0 12px;display:flex;align-items:center}
.btn-sub{display:inline-block;background:var(--green);color:var(--white);font-family:"Montserrat",Arial,sans-serif;font-size:12px;font-weight:600;padding:9px 18px;margin-top:10px}
.socials{display:flex;gap:8px;margin-top:22px}
.socials span{width:30px;height:30px;border:1.5px solid var(--white);border-radius:50%}
.copyright{position:absolute;left:0;bottom:0;width:1200px;height:56px;background:var(--navy-deep);color:#c9d2e0;font-size:12px;text-align:center;line-height:56px}
</style>
</head>
<body>

<header class="section hero">
  <div class="hero-photo" role="img" aria-label="Photograph of a lodge deck and wooden interior at dusk"></div>
  <div class="hero-shade"></div>
  <svg class="hero-edge" viewBox="0 0 1200 140" preserveAspectRatio="none" aria-hidden="true">
    <polygon points="0,0 600,70 1200,0 1200,140 0,140" fill="#ffffff"/>
    <polyline points="0,6 600,76 1200,6" fill="none" stroke="#25c35f" stroke-width="12"/>
  </svg>
  <div class="brand-bar"><span class="brand">Tavok Construction</span></div>
  <nav class="nav">
    <a class="active" href="#">HOME</a>
    <a href="#">ABOUT US</a>
    <a href="#">SERVICES</a>
    <a href="#">PROJECTS</a>
    <a href="#">NEWS</a>
    <a href="#">CONTACT US</a>
  </nav>
  <div class="hero-copy">
    <h1>TAVOK CONSTRUCTION</h1>
    <p>We are a Construction Company based in the Okavango Delta and specialize on Lodge building.</p>
    <a class="btn btn-green" href="#">READ MORE</a>
  </div>
</header>

<section class="section services">
  <div class="heading">
    <h2>OUR SERVICES</h2>
    <span class="rule"></span>
    <p class="intro">We plan, design and build lodges that sit lightly on the land and welcome guests for years.</p>
  </div>

  <article class="service-card" style="left:108px;top:190px">
    <svg class="service-icon" viewBox="0 0 48 48" aria-hidden="true"><path d="M8 38h32M14 38V20l10-8 10 8v18M20 38V28h8v10" fill="none" stroke="#25c35f" stroke-width="2.5" stroke-linejoin="round"/></svg>
    <h3>CONSTRUCTION</h3>
    <p>Timber and stone lodges raised with local crews, careful planning and materials made to last. <span class="more">READ MORE</span></p>
  </article>

  <article class="service-card right" style="left:730px;top:190px">
    <svg class="service-icon" viewBox="0 0 48 48" aria-hidden="true"><path d="M10 40l28-28M10 40l4-12 20-20 8 8-20 20z" fill="none" stroke="#25c35f" stroke-width="2.5" stroke-linejoin="round"/></svg>
    <h3>ARCHITECTURE</h3>
    <p>Drawings and site plans that follow the river, the trees and the light of each day. <span class="more">READ MORE</span></p>
  </article>

  <article class="service-card" style="left:108px;top:390px">
    <svg class="service-icon" viewBox="0 0 48 48" aria-hidden="true"><rect x="10" y="8" width="22" height="30" fill="none" stroke="#25c35f" stroke-width="2.5"/><path d="M16 16h10M16 22h10M16 28h6M30 30l8 8" fill="none" stroke="#25c35f" stroke-width="2.5"/></svg>
    <h3>RENOVATION</h3>
    <p>We repair, extend and refresh older camps so they feel new again for every season. <span class="more">READ MORE</span></p>
  </article>

  <article class="service-card right" style="left:730px;top:390px">
    <svg class="service-icon" viewBox="0 0 48 48" aria-hidden="true"><path d="M12 36l16-16M28 20a8 8 0 1 0 0-0.1M12 36l-3 3" fill="none" stroke="#25c35f" stroke-width="2.5" stroke-linecap="round"/><circle cx="32" cy="16" r="8" fill="none" stroke="#25c35f" stroke-width="2.5"/></svg>
    <h3>OTHER</h3>
    <p>Decks, walkways, water systems and solar power for remote sites across the whole delta. <span class="more">READ MORE</span></p>
  </article>

  <div class="worker" role="img" aria-label="Builder in a yellow hard hat and tool belt, arms folded"></div>
</section>

<section class="section about">
  <div class="about-copy">
    <h2>ABOUT TAVOK</h2>
    <span class="rule"></span>
    <p>Tavok Construction has built lodges, camps and guest houses in northern Botswana for many years. Our team knows the seasons, the floods and the sand, and we plan every project around them. From the first sketch to the final coat of varnish, we stay on site and keep our clients close.</p>
    <a class="btn btn-navy" href="#">READ MORE</a>
  </div>
  <div class="about-art" role="img" aria-label="Pencil sketch of a city skyline with cranes and a bulldozer"></div>
</section>

<section class="section projects">
  <div class="heading">
    <h2>OUR PROJECTS</h2>
    <span class="rule"></span>
    <p class="intro">A selection of lodges, camps and private homes we have completed across the Okavango region.</p>
  </div>
  <svg class="collage" viewBox="0 0 1200 555" role="img" aria-label="Diamond collage of completed lodge and cabin project photographs">
    <defs>
      <linearGradient id="wood" x1="0" y1="0" x2="0" y2="1"><stop offset="0" stop-color="#6d8fb8"/><stop offset=".5" stop-color="#7a4e2c"/><stop offset="1" stop-color="#3b2a1c"/></linearGradient>
      <linearGradient id="dusk" x1="0" y1="0" x2="1" y2="1"><stop offset="0" stop-color="#2b2a33"/><stop offset=".6" stop-color="#b8733a"/><stop offset="1" stop-color="#3a2517"/></linearGradient>
      <linearGradient id="city" x1="0" y1="0" x2="0" y2="1"><stop offset="0" stop-color="#8ec3ea"/><stop offset="1" stop-color="#3b4e63"/></linearGradient>
      <linearGradient id="forest" x1="0" y1="0" x2="1" y2="1"><stop offset="0" stop-color="#5c7a44"/><stop offset="1" stop-color="#6b4a2d"/></linearGradient>
    </defs>
    <polygon points="280,170 405,295 280,420 155,295" fill="url(#wood)"/>
    <polygon points="440,300 505,365 440,430 375,365" fill="#25c35f"/>
    <polygon points="560,180 650,270 560,360 470,270" fill="url(#dusk)"/>
    <polygon points="700,140 760,200 700,260 640,200" fill="url(#forest)"/>
    <polygon points="830,160 930,260 830,360 730,260" fill="url(#dusk)"/>
    <polygon points="690,270 790,370 690,470 590,370" fill="url(#city)"/>
    <polygon points="560,360 610,410 560,460 510,410" fill="url(#forest)"/>
    <polygon points="940,300 1010,370 940,440 870,370" fill="url(#wood)"/>
    <polygon points="830,380 880,430 830,480 780,430" fill="url(#dusk)"/>
  </svg>
</section>

<section class="section testimonial">
  <blockquote class="quote">
    <p>Tavok built our new lodge on time and with real care for the land around it. The crew worked through the rainy months without complaint, and every detail, from the roof thatch to the decks, was finished beautifully. Our guests love it and so do we.</p>
    <p class="name">LESEDI MOYO</p>
    <p class="role">Lodge owner, Maun</p>
  </blockquote>
  <div class="portrait" role="img" aria-label="Portrait photo of the client"></div>
</section>

<footer class="section footer">
  <div class="col" style="left:130px;width:280px">
    <p class="brand">Tavok Construction</p>
    <p style="margin-top:18px">We build lodges, camps and homes across northern Botswana with local hands, honest prices and a deep respect for the wild places we work in.</p>
    <p class="read">Read more</p>
  </div>
  <div class="col" style="left:480px;width:200px">
    <h3>CONTACT US</h3>
    <p class="label">ADDRESS</p>
    <p>Plot 214, Mophane Road<br>Maun, Botswana</p>
    <p class="label">PHONE</p>
    <p>+267 555 0142</p>
    <p class="label">Email</p>
    <p>hello@tavok.construction</p>
  </div>
  <div class="col" style="left:712px;width:140px">
    <h3>LINKS</h3>
    <ul>
      <li>Home</li>
      <li>About us</li>
      <li>Services</li>
      <li>Projects</li>
      <li>News</li>
      <li>Contact</li>
    </ul>
  </div>
  <div class="col" style="left:878px;width:260px">
    <h3>KEEP IN TOUCH</h3>
    <div class="email-field">EMAIL ADDRESS</div>
    <span class="btn-sub">SUBSCRIBE</span>
    <div class="socials"><span></span><span></span><span></span><span></span><span></span></div>
  </div>
  <p class="copyright">© Copyright 2020 Tavok Construction All right reserved</p>
</footer>

</body>
</html>
```